Advanced Therapeutic Massage Therapist

I need a business card advertising my massage services as an advanced therapeutic massage therapist. I offer advanced therapeutic massage, swedish and deep tissue. I want to create a simple, professional and feminine card. I like bright colours and creativity.

I prefer a bold and experimental approach rather than something status-quo. A card to suggest therapeutic healing through dynamic massage. Motifs, shapes or layout which suggest movement and flow.

Target Market(s)

Everybody!

Industry/Entity Type

Health And Wellness

Contact Information for Business Card

The card should include:
My name, logo, services offered and my contact details.

Siobhán Delaney
Massage Therapist

- Swedish - Deep Tissue - Advanced Therapeutic

Phone: (+353) 87 296 1740
Email: regenerate@siobhandelaney-example.com
Website: www.siobhandelany-example.com

Font styles to use
Serif
Sans Serif
Decorative
Script

Colors

Designer to choose colors to be used in the design.

Requirements
Must have
• An example may contain something like this, yet concise:
• "Siobhán Delaney
• Massage Therapist
• - Swedish - Deep Tissue - Advanced Therapeutic"
Nice to have
• This sentence is optional:
• Imagery such as a logo or symbol. I have attached a file containing a logo I had produced however the name is incorrect now as it is "Siobhán" not "Sadie". It could be edited to change it to Siobhán.
• I have sent the file as .psd .jpg. .pdf and .png
• I like when the card conveys energy, movement, pressure points, flow etc.
• I just like the designer to follow their own style and ideas. I like bright colours but must have a lot of a base colour to offset it. I really prefer them to follow their own inspiration. That is my preference.
Should not have
• Pine trees, non-native trees to Britain and Ireland, exotic flowers or animals that are not native to Britain and Ireland.
• I don't like brown as the background colour of the card.
• The cars shouldn't look like a wedding invitation i.e too many floral type designs.

```html
<!DOCTYPE html>
<html lang="en">
<head>
<meta charset="utf-8">
<title>Siobhán Delaney – Massage Therapist Business Card</title>
<link rel="stylesheet" href="https://fonts.googleapis.com/css2?family=Allura&family=Josefin+Sans:wght@300&family=Raleway:wght@300;400&family=Barlow+Condensed:wght@500&display=swap">
<style>
  :root {
    --stage: #686868;
    --card: #232323;
    --mint: #c4ebe4;
    --text-light: #dcdcdc;
    --teal: #9fd6ca;
    --green: #6fc4a3;
    --gold: #d9b24c;
    --gold-light: #f1d27a;
    --aqua: #a9d8cf;
  }
  * { margin: 0; padding: 0; box-sizing: border-box; }
  html, body { width: 1200px; height: 550px; overflow: hidden; }
  body { background: var(--stage); position: relative; }

  .card {
    position: absolute;
    top: 158px;
    width: 390px;
    height: 234px;
    background: var(--card);
    overflow: hidden;
    box-shadow: 0 0 0 1px rgba(255,255,255,0.08);
  }
  .card--front { left: 195px; }
  .card--back { left: 614px; }

  /* Front */
  .emblem {
    position: absolute;
    left: 137px; top: 32px;
    width: 116px; height: 116px;
    border-radius: 50%;
    background: radial-gradient(circle, var(--aqua) 55%, #b99448 85%, #6b4f2a 100%);
  }
  .front-name {
    position: absolute;
    left: 0; right: 0; top: 148px;
    text-align: center;
    font-family: "Allura", cursive;
    font-size: 27px;
    line-height: 1;
    color: #ffffff;
  }
  .front-role {
    position: absolute;
    left: 0; right: 0; top: 174px;
    text-align: center;
    font-family: "Josefin Sans", sans-serif;
    font-weight: 300;
    font-size: 9.5px;
    letter-spacing: 1px;
    color: var(--text-light);
  }
  .front-tagline {
    position: absolute;
    left: 0; right: 0; top: 209px;
    text-align: center;
    font-family: "Barlow Condensed", sans-serif;
    font-weight: 500;
    font-size: 11px;
    color: var(--green);
  }

  /* Back */
  .back-name {
    position: absolute;
    left: 18px; top: 26px;
    font-family: "Allura", cursive;
    font-size: 30px;
    line-height: 1;
    color: var(--mint);
  }
  .back-role {
    position: absolute;
    left: 19px; top: 58px;
    font-family: "Josefin Sans", sans-serif;
    font-weight: 300;
    font-size: 11px;
    letter-spacing: 1.2px;
    color: var(--text-light);
  }
  .contact-list {
    position: absolute;
    left: 19px; top: 154px;
    list-style: none;
    font-family: "Raleway", sans-serif;
    font-weight: 400;
    font-size: 10px;
    color: var(--text-light);
  }
  .contact-item {
    display: flex;
    align-items: center;
    gap: 9px;
    height: 17px;
  }
  .contact-icon { width: 9px; height: 9px; fill: var(--teal); flex: none; }
  .services {
    position: absolute;
    left: 19px; top: 210px;
    font-family: "Raleway", sans-serif;
    font-weight: 300;
    font-size: 10.5px;
    color: var(--teal);
  }
  .tree-decoration {
    position: absolute;
    left: 210px; top: 2px;
    width: 230px; height: 230px;
    border-radius: 50%;
    background: radial-gradient(circle at 40% 40%, var(--gold-light), var(--gold) 70%, #a8832e 100%);
  }
</style>
</head>
<body>

  <section class="card card--front" aria-label="Card front">
    <div class="emblem" role="img" aria-label="Circular emblem area in aqua and gold"></div>
    <p class="front-name">Siobhán Delaney</p>
    <p class="front-role">massage therapist</p>
    <p class="front-tagline">NTQB qualified, specializing in Advanced Therapeutic &amp; Deep Tissue Massage</p>
  </section>

  <section class="card card--back" aria-label="Card back">
    <p class="back-name">Siobhán Delaney</p>
    <p class="back-role">massage therapist</p>

    <ul class="contact-list">
      <li class="contact-item">
        <svg class="contact-icon" viewBox="0 0 10 10" aria-hidden="true"><path d="M1 3 Q5 0 9 3 L8 4.5 L6.5 4 L6.5 3 Q5 2.5 3.5 3 L3.5 4 L2 4.5 Z M2 5.5 H8 V9 H2 Z"/></svg>
        <span>(+353) 87 296 1740</span>
      </li>
      <li class="contact-item">
        <svg class="contact-icon" viewBox="0 0 10 10" aria-hidden="true"><path d="M0 2 H10 V8 H0 Z M0.8 2.6 L5 5.6 L9.2 2.6" stroke="#232323" stroke-width="0.8"/></svg>
        <span>siobhan@siobhandelaney-example.com</span>
      </li>
      <li class="contact-item">
        <svg class="contact-icon" viewBox="0 0 10 10" aria-hidden="true"><circle cx="5" cy="5" r="4.6"/><path d="M0.5 5 H9.5 M5 0.5 V9.5 M5 0.5 Q2 5 5 9.5 M5 0.5 Q8 5 5 9.5" stroke="#232323" stroke-width="0.7" fill="none"/></svg>
        <span>www.siobhandelany-example.com</span>
      </li>
    </ul>

    <p class="services">Swedish - Deep Tissue - Advanced Therapeutic</p>

    <div class="tree-decoration" role="img" aria-label="Large gold circular ornamental decoration"></div>
  </section>

</body>
</html>
```